Law Office needs stationery design and business card

I currently have been using the same letterhead for the last 8 years. Since i 'm about to adding another location, I want to revamp my letterhead and business card. I already have a logo i'm happy with. I will upload my current letterhead, fax sheet, envelope, and logos. I need a business card also. I have 2 locations, 1 phone number, 1 fax line, website, etc. If possible and fitting with the design, I would like to keep the same information listed currently on the letterhead.

**Keep in mind, I also NEED A FAX SHEET COVER. thank you

Hello, Please submit a Gray Scale or Black and White version of your designs also, since most of the time I will be printing NON color stationery. I will seldom use a color print for my letterhead, I would like to have a color version for my benefit, however i will print in grayscale majority of the time . For the Business Card, that can just be in color. When I get my business cards they will be in color.Thank youEnrique Added Sunday, September 18, 2016

```html
<!DOCTYPE html>
<html lang="en">
<head>
<meta charset="utf-8">
<title>Ashford Law – Business Card</title>
<link rel="stylesheet" href="https://fonts.googleapis.com/css2?family=Libre+Franklin:wght@400;500;600&display=swap">
<style>
  :root {
    --stage: #e8e5e1;
    --card: #161616;
    --card-edge: #262626;
    --gold: #c9a45c;
    --silver: #8a8a8a;
    --white: #f2f2f2;
    --rule: #9a9a9a;
  }
  * { box-sizing: border-box; margin: 0; padding: 0; }
  html, body {
    width: 1200px; height: 787px; overflow: hidden;
    background: var(--stage);
    font-family: "Libre Franklin", Arial, sans-serif;
  }
  .stage { position: relative; width: 1200px; height: 787px; }
  .card {
    position: absolute; top: 239px;
    width: 540px; height: 309px;
    background: var(--card);
    border: 1px solid var(--card-edge);
    border-radius: 4px;
    box-shadow: 0 6px 18px rgba(0,0,0,.25);
  }
  .card-front { left: 40px; }
  .card-back { left: 620px; }

  /* Front */
  .front-brand {
    position: absolute; left: 0; right: 0; top: 70px;
    display: flex; flex-direction: column; align-items: center; gap: 22px;
  }
  .brand-square {
    width: 34px; height: 34px; background: var(--silver);
    transform: rotate(45deg);
  }
  .front-name {
    color: var(--silver); font-size: 34px; font-weight: 500;
    letter-spacing: 2px; text-transform: uppercase; line-height: 1;
  }
  .front-web {
    position: absolute; left: 0; right: 0; top: 186px; text-align: center;
    color: var(--silver); font-size: 15px; letter-spacing: 4px;
  }
  .front-social {
    position: absolute; right: 18px; top: 18px;
    width: 18px; height: 18px; background: var(--gold);
  }

  /* Back */
  .person { position: absolute; left: 28px; top: 40px; }
  .person-name { color: var(--gold); font-size: 21px; font-weight: 500; white-space: nowrap; }
  .person-role { color: var(--white); font-size: 14px; margin-top: 4px; }
  .rule-top {
    position: absolute; left: 28px; top: 108px; width: 270px;
    border-top: 1px solid var(--rule);
  }
  .contacts { position: absolute; left: 28px; top: 124px; list-style: none; }
  .contacts li {
    display: flex; align-items: center; gap: 9px;
    color: var(--white); font-size: 14px; height: 24px;
  }
  .contacts svg { width: 14px; height: 14px; fill: var(--gold); flex: none; }

  .back-brand {
    position: absolute; right: 28px; top: 68px; width: 200px;
    display: flex; flex-direction: column; align-items: center; gap: 18px;
  }
  .back-brand .brand-square { background: var(--gold); width: 30px; height: 30px; }
  .back-name {
    color: var(--gold); font-size: 26px; font-weight: 500;
    letter-spacing: 1.5px; text-transform: uppercase; line-height: 1;
    white-space: nowrap;
  }
  .rule-bottom {
    position: absolute; right: 28px; top: 186px; width: 230px;
    border-top: 1px solid var(--rule);
  }
  .offices { position: absolute; right: 28px; top: 198px; list-style: none; }
  .offices li {
    display: flex; align-items: center; justify-content: flex-end; gap: 10px;
    color: var(--white); font-size: 14px; line-height: 19px; text-align: right;
    margin-bottom: 10px;
  }
  .offices svg { width: 14px; height: 18px; fill: var(--gold); flex: none; }
</style>
</head>
<body>
<main class="stage">
  <section class="card card-front">
    <span class="front-social"></span>
    <div class="front-brand">
      <span class="brand-square"></span>
      <span class="front-name">Ashford Law</span>
    </div>
    <p class="front-web">www.AshfordLaw.com</p>
  </section>

  <section class="card card-back">
    <div class="person">
      <p class="person-name">Maren Holt Davenport Esq.</p>
      <p class="person-role">Attorney</p>
    </div>
    <div class="rule-top"></div>
    <ul class="contacts">
      <li><svg viewBox="0 0 16 16"><path d="M3 1h3l1.5 4-2 1.3a9 9 0 0 0 4.2 4.2L11 8.5l4 1.5v3a2 2 0 0 1-2 2A12 12 0 0 1 1 3a2 2 0 0 1 2-2z"/></svg>555.210.4471</li>
      <li><svg viewBox="0 0 16 16"><path d="M4 1h8v4H4zM1 6h14v7h-3v2H4v-2H1zm4 5v3h6v-3z"/></svg>555.382.6620</li>
      <li><svg viewBox="0 0 16 16"><path d="M1 3h14v10H1zm1.5 1.2v.6L8 9l5.5-4.2v-.6z"/></svg>Maren@AshfordLaw.com</li>
      <li><svg viewBox="0 0 16 16"><circle cx="8" cy="8" r="7"/><path d="M1 8h14M8 1c3 3 3 11 0 14M8 1c-3 3-3 11 0 14" stroke="#161616" stroke-width="1.2" fill="none"/></svg>www.AshfordLaw.com</li>
    </ul>

    <div class="back-brand">
      <span class="brand-square"></span>
      <span class="back-name">Ashford Law</span>
    </div>
    <div class="rule-bottom"></div>
    <ul class="offices">
      <li><span>48 Alder Row<br>Suite 300, Brookfield, PA 19000</span><svg viewBox="0 0 14 18"><path d="M7 0a7 7 0 0 1 7 7c0 5-7 11-7 11S0 12 0 7a7 7 0 0 1 7-7zm0 4a3 3 0 1 0 0 6 3 3 0 0 0 0-6z"/></svg></li>
      <li><span>730 Linden St.<br>Harlow, PA 19002</span><svg viewBox="0 0 14 18"><path d="M7 0a7 7 0 0 1 7 7c0 5-7 11-7 11S0 12 0 7a7 7 0 0 1 7-7zm0 4a3 3 0 1 0 0 6 3 3 0 0 0 0-6z"/></svg></li>
    </ul>
  </section>
</main>
</body>
</html>
```